Pellmore Heating & Air

I need a business card made for my company. I would like my new logo for Pellmore Heating and Air on the front and my Garage Door on the back.
Front to say -Heating & Air Conditioning , Mini Splits and Heat Pumps, Hydronic In-Floor Heat. Locally Owned and Operated! Licensed, Boned and Insured. Free Estimates on new equipment. 555-201-4837
KVB Back Card, change phone# to 555-318-6024. Remove Commercial and residential and fully sticked vans lines.

```html
<!DOCTYPE html>
<html lang="en">
<head>
<meta charset="utf-8">
<title>Pellmore Heating &amp; Air – Business Card</title>
<link rel="stylesheet" href="https://fonts.googleapis.com/css2?family=Open+Sans:wght@400;600;700;800&display=swap">
<style>
  :root {
    --brand-blue: #0c4f8c;
    --brand-red: #ea2b24;
    --card-white: #ffffff;
    --backdrop: #e6e8eb;
    --text-light: #ffffff;
    --card-shadow: 0 14px 30px rgba(0, 0, 0, 0.22);
  }
  * { box-sizing: border-box; margin: 0; padding: 0; }
  html, body {
    width: 1200px;
    height: 1125px;
    overflow: hidden;
    background: var(--backdrop);
    font-family: "Open Sans", Arial, sans-serif;
  }
  .canvas {
    position: relative;
    width: 1200px;
    height: 1125px;
  }
  .card {
    position: absolute;
    left: 160px;
    width: 880px;
    height: 503px;
    box-shadow: var(--card-shadow);
    overflow: hidden;
  }
  /* Front */
  .card-front {
    top: 40px;
    background: var(--brand-blue);
    color: var(--text-light);
  }
  .front-name {
    position: absolute;
    left: 60px;
    top: 250px;
    width: 370px;
    font-weight: 800;
    font-size: 42px;
    line-height: 1.08;
    color: var(--text-light);
    text-transform: uppercase;
    letter-spacing: 0.5px;
  }
  .front-divider {
    position: absolute;
    left: 448px;
    top: 120px;
    width: 2px;
    height: 190px;
    background: var(--brand-red);
  }
  .service-list {
    position: absolute;
    left: 482px;
    top: 118px;
    list-style: none;
    font-size: 21px;
    line-height: 32px;
    font-weight: 400;
  }
  .service-list li {
    position: relative;
    padding-left: 20px;
  }
  .service-list li::before {
    content: "";
    position: absolute;
    left: 0;
    top: 14px;
    width: 7px;
    height: 7px;
    border-radius: 50%;
    background: var(--brand-red);
  }
  .front-phone {
    position: absolute;
    left: 482px;
    top: 378px;
    display: flex;
    align-items: center;
    gap: 12px;
    font-size: 32px;
    font-weight: 700;
    color: var(--text-light);
  }
  /* Back */
  .card-back {
    top: 582px;
    background: var(--card-white);
  }
  .back-name {
    position: absolute;
    left: 70px;
    top: 190px;
    width: 370px;
    font-weight: 800;
    font-size: 40px;
    line-height: 1.1;
    color: var(--brand-blue);
    text-transform: uppercase;
  }
  .back-divider {
    position: absolute;
    left: 462px;
    top: 150px;
    width: 2px;
    height: 150px;
    background: var(--brand-blue);
  }
  .back-phone {
    position: absolute;
    left: 500px;
    top: 198px;
    display: flex;
    align-items: center;
    gap: 12px;
    font-size: 32px;
    font-weight: 700;
    color: var(--brand-blue);
  }
  .footer-band {
    position: absolute;
    left: 0;
    bottom: 0;
    width: 880px;
    height: 34px;
  }
  .phone-icon { width: 30px; height: 30px; flex: none; }
</style>
</head>
<body>
<div class="canvas">

  <section class="card card-front">
    <div class="front-name">Pellmore<br>Heating &amp; Air</div>
    <div class="front-divider"></div>
    <ul class="service-list">
      <li>Heating &amp; Air Conditioning</li>
      <li>Mini Splits and Heat Pumps</li>
      <li>Hydronic In-Floor Heat</li>
      <li>Locally Owned and Operated</li>
      <li>Licensed, Boned and Insured</li>
      <li>Free Estimates on new equipment.</li>
    </ul>
    <div class="front-phone">
      <svg class="phone-icon" viewBox="0 0 24 24" aria-hidden="true">
        <path fill="#ea2b24" d="M6.6 10.8a15.1 15.1 0 0 0 6.6 6.6l2.2-2.2a1 1 0 0 1 1-.25 11.4 11.4 0 0 0 3.6.57 1 1 0 0 1 1 1V20a1 1 0 0 1-1 1A17 17 0 0 1 3 4a1 1 0 0 1 1-1h3.5a1 1 0 0 1 1 1c0 1.25.2 2.45.57 3.6a1 1 0 0 1-.25 1z"/>
      </svg>
      <span>555-201-4837</span>
    </div>
  </section>

  <section class="card card-back">
    <div class="back-name">Kelvane<br>Garage Door</div>
    <div class="back-divider"></div>
    <div class="back-phone">
      <svg class="phone-icon" viewBox="0 0 24 24" aria-hidden="true">
        <path fill="#ea2b24" d="M6.6 10.8a15.1 15.1 0 0 0 6.6 6.6l2.2-2.2a1 1 0 0 1 1-.25 11.4 11.4 0 0 0 3.6.57 1 1 0 0 1 1 1V20a1 1 0 0 1-1 1A17 17 0 0 1 3 4a1 1 0 0 1 1-1h3.5a1 1 0 0 1 1 1c0 1.25.2 2.45.57 3.6a1 1 0 0 1-.25 1z"/>
      </svg>
      <span>555-318-6024</span>
    </div>
    <svg class="footer-band" viewBox="0 0 880 34" preserveAspectRatio="none" aria-hidden="true">
      <polygon points="0,0 490,0 470,34 0,34" fill="#0c4f8c"/>
      <polygon points="498,0 880,0 880,34 478,34" fill="#ea2b24"/>
    </svg>
  </section>

</div>
</body>
</html>
```